bottle label/ product label for smoothies (ultra fresh)

Please create a bottle label for our smoothies for retail distribution.
It's important that the following key features are clearly stated:

Ultra-fresh

Handmade

No preservatives

Not heat-treated

No added sugar

The base of the product label should be transparent, so that the color and content of the smoothie can be seen clearly.

We are a young, dynamic company. Our values are honesty, ultra-freshness, and authenticity — and we are the only ones producing this type of product in our country. We are positioned in the premium segment.

Design style: Modern, clean, and natural — but not playful or childish.

Example product: Kelu Kelu (Mango, Pineapple, Lemon, Passion Fruit, Orange)

Wenn du möchtest, kann ich auch gleich einen konkreten Vorschlag für das Etikettendesign auf Englisch oder einen Entwurfstext für das Label selbst erstellen. Sag einfach Bescheid!

Target Market(s)

trade - convenience

Industry/Entity Type

trade

Font styles to use
Sans Serif

Requirements
Must have
• sales- features: Ultra-fresh Handmade No preservatives Not heat-treated No added sugar

```html
<!DOCTYPE html>
<html lang="en">
<head>
<meta charset="utf-8">
<title>lumora – Passion Fruit Smoothie Label</title>
<link href="https://fonts.googleapis.com/css2?family=Nunito:wght@700&family=Alfa+Slab+One&family=Pacifico&family=Roboto+Condensed:wght@500;700&display=swap" rel="stylesheet">
<style>
  :root {
    --canvas: #ececec;
    --label-clear: rgba(255,255,255,0.55);
    --brand-red: #c3213a;
    --title-yellow: #f7c21a;
    --title-shade: #e39a12;
    --fresh-green: #2e8b3e;
    --juice-light: #fde27a;
    --juice-deep: #f3b21c;
    --fruit-purple: #7a1e3e;
    --white: #ffffff;
  }
  * { margin: 0; padding: 0; box-sizing: border-box; }
  html, body { width: 1200px; height: 1200px; overflow: hidden; background: var(--canvas); }
  .label {
    position: absolute; left: 406px; top: 50px; width: 388px; height: 1100px;
    background: var(--label-clear); overflow: hidden;
  }
  .brand-band { position: absolute; left: 0; top: 0; width: 388px; height: 135px; }
  .brand-name {
    position: absolute; left: 0; right: 0; top: 40px; text-align: center;
    font-family: "Nunito", sans-serif; font-weight: 700; font-size: 70px;
    color: var(--white); line-height: 1; letter-spacing: 1px;
  }
  .product-title {
    position: absolute; left: 30px; top: 148px; width: 340px;
    font-family: "Alfa Slab One", serif; color: var(--title-yellow);
    text-shadow: 2px 2px 0 var(--title-shade); line-height: 1;
  }
  .product-title .line-1 { display: block; font-size: 60px; }
  .product-title .line-2 { display: block; font-size: 52px; margin-top: 4px; }
  .product-type {
    position: absolute; left: 130px; top: 238px;
    font-family: "Pacifico", cursive; font-size: 44px; color: var(--brand-red);
    text-shadow: 0 0 4px var(--white), 0 0 4px var(--white);
  }
  .claim-rule { position: absolute; left: 0; top: 392px; width: 388px; height: 30px; }
  .claim-text {
    position: absolute; left: 0; right: 0; top: 397px; text-align: center;
    font-family: "Roboto Condensed", sans-serif; font-weight: 500; font-size: 19px;
    color: var(--fresh-green); letter-spacing: 0.5px;
  }
  .claim-text u { text-underline-offset: 3px; }
  .feature-icons { position: absolute; left: 0; top: 468px; width: 388px; height: 90px; }
  .fruit-art {
    position: absolute; left: 0; top: 620px; width: 388px; height: 480px;
    background:
      radial-gradient(circle at 45% 30%, var(--fruit-purple) 0 60px, transparent 62px),
      radial-gradient(circle at 70% 35%, #f0a32a 0 40px, transparent 42px),
      linear-gradient(180deg, rgba(253,226,122,0) 0%, var(--juice-light) 55%, var(--juice-deep) 100%);
  }
  .fresh-badge { position: absolute; left: 4px; top: 958px; width: 120px; height: 90px; }
  .volume {
    position: absolute; left: 290px; top: 1045px; padding: 3px 8px;
    background: var(--white); border-radius: 14px;
    font-family: "Roboto Condensed", sans-serif; font-weight: 700; font-size: 18px;
    color: var(--brand-red);
  }
</style>
</head>
<body>
<main class="label">
  <svg class="brand-band" viewBox="0 0 388 135" aria-hidden="true">
    <path d="M0 0 H388 V62 C360 62 350 135 300 135 H88 C38 135 28 62 0 62 Z" fill="var(--brand-red)"/>
  </svg>
  <div class="brand-name">lumora</div>

  <h1 class="product-title"><span class="line-1">PASSION</span><span class="line-2">FRUIT</span></h1>
  <div class="product-type">smoothie</div>

  <svg class="claim-rule" viewBox="0 0 388 30" aria-hidden="true">
    <line x1="0" y1="15" x2="80" y2="15" stroke="var(--fresh-green)" stroke-width="2"/>
    <line x1="308" y1="15" x2="388" y2="15" stroke="var(--fresh-green)" stroke-width="2"/>
    <rect x="80" y="2" width="228" height="26" rx="13" fill="none" stroke="var(--fresh-green)" stroke-width="2"/>
  </svg>
  <div class="claim-text"><u>NO</u> PRESERVATIVES</div>

  <svg class="feature-icons" viewBox="0 0 388 90" font-family="Roboto Condensed, sans-serif" font-weight="700" text-anchor="middle">
    <g class="icon-handmade">
      <circle cx="68" cy="42" r="38" fill="none" stroke="var(--fresh-green)" stroke-width="3"/>
      <path d="M56 62 V34 a4 4 0 0 1 8 0 V48 M64 30 a4 4 0 0 1 8 0 V48 M72 34 a4 4 0 0 1 8 0 V56 q0 10 -12 10 h-6 q-6 0 -6 -4" fill="none" stroke="var(--fresh-green)" stroke-width="2.5"/>
      <text x="68" y="22" font-size="10" fill="var(--fresh-green)">HANDMADE</text>
    </g>
    <g class="icon-sugar-free">
      <circle cx="194" cy="42" r="38" fill="none" stroke="var(--fresh-green)" stroke-width="3"/>
      <rect x="176" y="22" width="18" height="18" fill="none" stroke="var(--fresh-green)" stroke-width="2"/>
      <rect x="194" y="28" width="18" height="18" fill="none" stroke="var(--fresh-green)" stroke-width="2"/>
      <line x1="170" y1="18" x2="218" y2="52" stroke="var(--fresh-green)" stroke-width="2.5"/>
      <rect x="164" y="54" width="60" height="24" rx="6" fill="var(--fresh-green)"/>
      <text x="194" y="65" font-size="10" fill="var(--white)">SUGAR</text>
      <text x="194" y="75" font-size="10" fill="var(--white)">FREE</text>
    </g>
    <g class="icon-no-heat">
      <circle cx="321" cy="42" r="38" fill="none" stroke="var(--fresh-green)" stroke-width="3"/>
      <path d="M321 26 q12 14 6 26 q-6 8 -12 0 q-6 -10 6 -26 Z" fill="none" stroke="var(--fresh-green)" stroke-width="2"/>
      <line x1="300" y1="22" x2="342" y2="62" stroke="var(--fresh-green)" stroke-width="2.5"/>
      <text x="321" y="20" font-size="9" fill="var(--fresh-green)">NO HEAT</text>
      <text x="321" y="74" font-size="9" fill="var(--fresh-green)">TREATED</text>
    </g>
  </svg>

  <div class="fruit-art" role="img" aria-label="Illustration of whole and halved passion fruits with leaves in a golden juice splash"></div>

  <svg class="fresh-badge" viewBox="0 0 120 90" font-family="Roboto Condensed, sans-serif" font-weight="700" text-anchor="middle">
    <path d="M4 88 C0 40 40 4 118 4 C118 60 80 88 4 88 Z" fill="var(--fresh-green)" stroke="var(--white)" stroke-width="3"/>
    <text x="56" y="44" font-size="19" fill="var(--white)">ULTRA</text>
    <text x="60" y="66" font-size="19" fill="var(--white)">FRESH</text>
  </svg>

  <div class="volume">400ml</div>
</main>
</body>
</html>
```